British Columbia Day banner showcasing 20% off site

Banner graphic promoting our BC Day sale
Size: 1800 x 1000
- flag has been uploaded for inspiration
- examples from other companies and their sale banners have been uploaded for inspiration.
- product images can be found at www.mygreenleafhub.com, please use a variety of different products in this banner

Target Market(s)

19+

Industry/Entity Type

Cannabis

Requirements
Must have
• Phrases:
- “Celebrate BC Day with BC bud and companies”
- “20% off site wide sale*"
- Underneath phrase the date of sale “July 30th - August 3rd”
- In tiny print “*excludes all sale and bundled items”
- MUST BE 1800 X1000
Nice to have
• - images of the products or bud we carry which can be found at www.mygreenleafhub.com
- bold
Should not have
• - company logo

```html
<!DOCTYPE html>
<html lang="en">
<head>
<meta charset="utf-8">
<title>BC Day Sale Banner</title>
<link href="https://fonts.googleapis.com/css2?family=Montserrat:ital,wght@0,500;0,700;0,800;0,900;1,500&display=swap" rel="stylesheet">
<style>
  :root {
    --brand-green: #43ad62;
    --ink: #333333;
    --muted: #7a7a7a;
    --paper: #ffffff;
    --leaf-dark: #2f5d34;
    --leaf-mid: #4f8f45;
    --leaf-light: #7cbf5c;
  }
  * { margin: 0; padding: 0; box-sizing: border-box; }
  html, body { width: 1200px; height: 667px; overflow: hidden; background: var(--paper); }
  .banner {
    position: relative;
    width: 1200px;
    height: 667px;
    background: var(--paper);
    font-family: "Montserrat", sans-serif;
    overflow: hidden;
  }
  .hero-photo {
    position: absolute;
    left: 0; top: 0;
    width: 600px; height: 667px;
    background:
      radial-gradient(ellipse at 45% 35%, var(--leaf-light) 0%, var(--leaf-mid) 40%, transparent 75%),
      linear-gradient(160deg, #4f7f55 0%, var(--leaf-mid) 45%, var(--leaf-dark) 100%);
  }
  .headline {
    position: absolute;
    left: 678px; top: 38px;
    font-weight: 900;
    font-size: 61px;
    line-height: 59px;
    letter-spacing: -0.5px;
    color: var(--ink);
  }
  .headline .accent { color: var(--brand-green); }
  .offer {
    position: absolute;
    left: 680px; top: 310px;
    font-weight: 800;
    font-size: 31px;
    color: var(--ink);
    white-space: nowrap;
  }
  .offer .discount {
    color: var(--brand-green);
    border-bottom: 2px solid var(--brand-green);
    padding-bottom: 1px;
  }
  .dates {
    position: absolute;
    left: 682px; top: 355px;
    font-weight: 800;
    font-size: 20px;
    color: var(--ink);
  }
  .fine-print {
    position: absolute;
    left: 681px; top: 389px;
    font-weight: 500;
    font-style: italic;
    font-size: 14px;
    color: var(--muted);
  }
  .shop-button {
    position: absolute;
    left: 683px; top: 431px;
    width: 214px; height: 56px;
    background: var(--brand-green);
    color: var(--paper);
    font-weight: 800;
    font-size: 18px;
    display: flex; align-items: center; justify-content: center;
    text-decoration: none;
    letter-spacing: 0.3px;
  }
  .product-row {
    position: absolute;
    left: 676px; top: 512px;
    width: 490px; height: 116px;
  }
</style>
</head>
<body>
  <div class="banner">
    <div class="hero-photo" role="img" aria-label="Close-up photo of a green cannabis plant with serrated leaves"></div>

    <h1 class="headline">
      <span class="accent">Celebrate</span><br>
      <span class="accent">BC Day with</span><br>
      BC bud and<br>
      companies
    </h1>

    <p class="offer"><span class="discount">20% off</span> site wide sale</p>
    <p class="dates">July 30th - August 3rd</p>
    <p class="fine-print">*Excludes all sale and bundled items</p>

    <a class="shop-button" href="#">SHOP NOW</a>

    <svg class="product-row" viewBox="0 0 490 116" role="img" aria-label="Row of six product photos of dried cannabis buds">
      <ellipse cx="28" cy="58" rx="24" ry="54" fill="#8a8a3c"/>
      <ellipse cx="114" cy="58" rx="30" ry="54" fill="#7a6f78"/>
      <ellipse cx="218" cy="58" rx="26" ry="54" fill="#7f8a4a"/>
      <ellipse cx="303" cy="58" rx="27" ry="54" fill="#5c4a55"/>
      <ellipse cx="385" cy="58" rx="25" ry="54" fill="#8a9256"/>
      <ellipse cx="466" cy="58" rx="26" ry="54" fill="#6f7a45"/>
    </svg>
  </div>
</body>
</html>
```